Ned Walcott Fairway Lessons Rack Card

The flyer will be a rack card. Front side only. Nothing on back. 3.75 inches by 8.5 inches. Or close to that. I’d like it to be as colorful as possible and to include several logos in different places.
The brochure is to attract golfers attention and still look traditional and classy not crazy or to artsy. Golf is a very traditional sport and would just like it to look professional and welcoming so golfers no I’m credible in my teaching and they will learn something. I will send a rough idea and a sample of one I had before but use your creative skills and ingenuity to design it. You will have to put my name: Ned Walcott under the TLQ logo. It is a requirement by the TLQ. Also the logo size must me .0875 inches high. If possible use a gotham or Hoefler text type or something businesslike or similar for my name. Also I am sorry for the different logos available on this file because I am not tech savvy so you will have to choose the best logo and cut it out of the grouping to match what you want to do. I am sorry for all the details. I will be available all weekend if you need more info. or help. I am sure you are very skilled and can tell I am not. Sorry. I laid out a sketch for you so you know what info. verbiage is important. and where to somewhat place the logos. Up to your skill for most of it. Your design! Go for it.!

Target Market(s)

Golfers of all ages from 18-70. Men and Women.

Industry/Entity Type

Golf Industry. Teaching and learning game if golf

Font styles to use
Sans Serif
Other font styles liked:
• Mixture maybe traditional type. Easy to read.

Colors

Designer to choose only greyscale colors for use in the design.

Requirements
Must have
• My JPG golf logo and the TLQ official logo. Also will send several other logos to put in. I will tell you where they should go on the rack card.
Nice to have
• Maybe a golf picture from a course with a green and flag as the one on my old brochure I’m sending or similar. It just adds color and eye catching
Should not have
• Nothing hard to read or difficult to comprehend. Pretty straight forward and quality and style in a traditional sense,

```html
<!DOCTYPE html>
<html lang="en">
<head>
<meta charset="utf-8">
<title>Ned Walcott Fairway Lessons – Rack Card</title>
<link href="https://fonts.googleapis.com/css2?family=Montserrat:wght@400;500;600;700;800&display=swap" rel="stylesheet">
<style>
  :root{
    --accent:#6b6b6b;
    --accent-soft:#bdbdbd;
    --accent-text:#4d4d4d;
    --ink:#1c1c1c;
    --text:#333333;
    --paper:#f0f0f0;
    --white:#ffffff;
    --stage:#d9d9d9;
    --sky:#cfcfcf;
    --hill:#8a8a8a;
    --grass:#9a9a9a;
    --seal-light:#9c9c9c;
    --seal-dark:#3a3a3a;
    --partner-light:#7a7a7a;
  }
  *{margin:0;padding:0;box-sizing:border-box}
  html,body{width:1200px;height:2388px;overflow:hidden}
  body{background:var(--stage);font-family:"Montserrat",Arial,sans-serif;color:var(--text);position:relative}
  .rack-card{position:absolute;left:92px;top:44px;width:1016px;height:2300px;overflow:hidden;background:var(--paper);box-shadow:0 10px 30px rgba(0,0,0,.25)}
  .course-photo{position:absolute;left:0;top:0;width:1016px;height:940px;
    background:linear-gradient(180deg,var(--sky) 0%,#c2c2c2 30%,var(--hill) 42%,#a5a5a5 50%,var(--grass) 75%,#858585 100%)}
  .shapes{position:absolute;left:0;top:0}
  .fill-paper{fill:var(--paper)}
  .fill-white{fill:var(--white)}
  .fill-accent{fill:var(--accent)}
  .fill-ink{fill:var(--ink)}
  .fill-seal-light{fill:var(--seal-light)}
  .fill-seal-dark{fill:var(--seal-dark)}
  .ring-soft{fill:none;stroke:var(--accent-soft);stroke-width:8}
  .icon-disc{fill:var(--accent);stroke:var(--white);stroke-width:3}
  .icon-line{fill:none;stroke:var(--white);stroke-width:2.5;stroke-linejoin:round;stroke-linecap:round}
  .t{position:absolute;transform:translate(-50%,-50%);white-space:nowrap;line-height:1.15}
  .l{position:absolute;transform:translateY(-50%);white-space:nowrap;line-height:1.15}
  .brand-name{color:var(--accent-text);font-weight:700;font-size:46px;text-align:center;line-height:1.1;white-space:normal;width:380px}
  .section-title{color:var(--accent-text);font-weight:700;font-size:36px;letter-spacing:2px}
  .price-pill{border:3px solid var(--accent);border-radius:40px;padding:4px 40px;font-weight:700;font-size:34px;color:var(--text);background:var(--white)}
  .price-pill sup{font-size:.55em}
  .muted{font-size:29px;letter-spacing:1px}
  .reg{font-weight:700;font-size:31px;letter-spacing:1px;color:var(--ink)}
  .reg sup{font-size:.55em}
  .offer{font-size:30px;letter-spacing:1.5px}
  .offer b{color:var(--accent);font-weight:500}
  .rule-short{position:absolute;height:3px;background:var(--accent)}
  .divider{position:absolute;width:3px;background:var(--accent)}
  .pill-label{border-radius:30px;padding:4px 22px;font-weight:700;font-size:26px;letter-spacing:3px;color:var(--white)}
  .pill-accent{background:var(--accent)}
  .pill-dark{background:var(--ink)}
  .level{color:var(--white);font-size:30px;line-height:1.2}
  .level b{font-weight:700}
  .more-info{color:var(--white);font-size:30px;line-height:1.2}
  .more-info b{font-weight:700;font-size:26px;letter-spacing:.5px}
  .includes-list{position:absolute;left:509px;top:1108px;list-style:none;font-size:27px;letter-spacing:1px;line-height:1.2}
  .includes-list li{position:relative;padding-left:28px;margin-bottom:10px}
  .includes-list li::before{content:"";position:absolute;left:0;top:12px;width:11px;height:11px;border-radius:50%;background:var(--accent)}
  .partner{font-weight:800;font-size:50px;letter-spacing:-1px}
  .partner-a{color:var(--partner-light)}
  .partner-b{color:var(--ink)}
  .package-title{font-weight:700;font-size:36px;letter-spacing:2px;color:var(--white)}
  .lesson-count{font-size:27px;letter-spacing:2px;color:#ececec}
  .pkg-pill{border:3px solid var(--white);border-radius:40px;padding:2px 30px;font-weight:700;font-size:33px;color:var(--white)}
  .pkg-pill sup,.reg-light sup{font-size:.55em}
  .reg-light{font-weight:700;font-size:31px;letter-spacing:1px;color:var(--white)}
  .deal{font-size:30px;letter-spacing:1.5px;color:var(--white)}
  .pkg-item{font-size:27px;letter-spacing:1px;color:var(--white)}
  .credential{font-size:26px;letter-spacing:1.5px;color:var(--text);text-align:center;line-height:1.18}
  .member-name{font-size:24px;letter-spacing:1.5px;color:var(--text)}
  .contact{font-size:26px;letter-spacing:1.5px;color:var(--white)}
  .contact b{font-weight:700}
  .sep{color:var(--accent-soft)}
</style>
</head>
<body>
<div class="rack-card">
  <div class="course-photo" role="img" aria-label="Photo of a golf green with a flag on its pin beside a standing golf bag full of clubs, trees and hills in the background"></div>

  <svg class="shapes" width="1016" height="2300" viewBox="0 0 1016 2300" aria-hidden="true">
    <path class="fill-paper" d="M0 904 Q 420 800 1016 842 V2300 H0 Z"/>
    <circle class="ring-soft" cx="766" cy="179" r="280"/>
    <circle class="fill-white" cx="766" cy="179" r="272"/>
    <path class="fill-accent" d="M0 1051 H330 A118.5 118.5 0 0 1 330 1288 H0 Z"/>
    <path class="fill-white" d="M0 1345 C 90 1285 250 1322 600 1322 C 800 1322 950 1300 1016 1292 V1560 H0 Z"/>
    <path class="fill-accent" d="M0 1482 Q 520 1452 1016 1490 V1826 H0 Z"/>
    <rect class="fill-ink" x="0" y="1824" width="1016" height="6"/>
    <rect class="fill-ink" x="0" y="2135" width="1016" height="165"/>
    <circle class="fill-seal-light" cx="191" cy="1966" r="86"/>
    <circle class="fill-seal-dark" cx="191" cy="1966" r="70"/>
    <circle class="fill-seal-light" cx="191" cy="1966" r="52"/>
    <circle class="fill-seal-light" cx="509" cy="1958" r="78"/>
    <circle class="fill-seal-dark" cx="509" cy="1958" r="64"/>
    <circle class="fill-seal-light" cx="509" cy="1958" r="38"/>
    <circle class="icon-disc" cx="191" cy="2132" r="25"/>
    <circle class="icon-disc" cx="509" cy="2132" r="25"/>
    <circle class="icon-disc" cx="828" cy="2132" r="25"/>
    <g class="icon-line">
      <rect x="179" y="2123" width="24" height="17" rx="2"/>
      <path d="M179 2124 L191 2133 L203 2124"/>
      <path d="M500 2121 c3 -2 6 0 7 3 l1 3 c0 2 -2 3 -3 4 c2 4 5 7 9 9 c1 -1 2 -3 4 -3 l3 1 c3 1 5 4 3 7 c-2 3 -6 4 -10 2 c-7 -3 -13 -9 -16 -16 c-2 -4 -1 -8 2 -10 z"/>
      <circle cx="828" cy="2132" r="12"/>
      <ellipse cx="828" cy="2132" rx="5" ry="12"/>
      <path d="M816 2132 H840 M818 2126 H838 M818 2138 H838"/>
    </g>
  </svg>

  <div class="t brand-name" style="left:766px;top:185px">Ned Walcott Fairway Lessons</div>

  <div class="t section-title" style="left:508px;top:872px">GOLF SWING ANALYSIS</div>
  <div class="t price-pill" style="left:269px;top:932px">$59<sup>99</sup></div>
  <div class="t muted" style="left:269px;top:994px">(1-Hour Analysis)</div>
  <div class="divider" style="left:509px;top:907px;height:98px"></div>
  <div class="t offer" style="left:742px;top:929px"><b>*</b>One Time Limited Offer</div>
  <div class="rule-short" style="left:702px;top:961px;width:80px"></div>
  <div class="t reg" style="left:742px;top:994px">REG <sup>$</sup>79<sup>00</sup></div>

  <div class="l level" style="left:56px;top:1127px"><b>Beginners</b><br>to <b>Advanced</b></div>
  <div class="l more-info" style="left:56px;top:1220px">Additional Info @<br><b>WWW.NWALCOTT.COM</b></div>

  <div class="t pill-label pill-accent" style="left:577px;top:1072px">INCLUDES</div>
  <ul class="includes-list">
    <li>Swing Analysis w/Video</li>
    <li>Review Of Swing Technique</li>
    <li>Suggested Tips &amp; Drills</li>
    <li>Video and Summary sent to<br>your mobile devices</li>
  </ul>

  <div class="t partner partner-a" style="left:325px;top:1399px">Swingmetric</div>
  <div class="t partner partner-b" style="left:722px;top:1399px">Launchvue</div>

  <div class="t package-title" style="left:508px;top:1513px">SPECIAL LESSON PACKAGE</div>
  <div class="t lesson-count" style="left:269px;top:1573px">3-ONE HOUR LESSONS</div>
  <div class="t reg-light" style="left:269px;top:1637px">REG <sup>$</sup>237<sup>00</sup></div>
  <div class="divider" style="left:509px;top:1557px;height:98px;background:var(--ink)"></div>
  <div class="t pkg-pill" style="left:747px;top:1576px"><sup>$</sup>225<sup>00</sup></div>
  <div class="t deal" style="left:747px;top:1638px">(Limited Deal)</div>
  <div class="t pill-label pill-dark" style="left:509px;top:1695px">INCLUDES</div>
  <div class="t pkg-item" style="left:508px;top:1749px">• Video Analysis &nbsp; • Lesson Summary And Video Review Sent To</div>
  <div class="t pkg-item" style="left:508px;top:1782px">Mobile Devices &nbsp; • Tips And Drills &nbsp; • Action Plan To Improve</div>

  <div class="t member-name" style="left:509px;top:2057px">NED WALCOTT</div>
  <div class="t credential" style="left:828px;top:1920px">NED WALCOTT<br>CLASS A MEMBER<br>QTR</div>
  <div class="rule-short" style="left:788px;top:1980px;width:80px"></div>
  <div class="t credential" style="left:828px;top:2025px">CENTURY<br>MEMBER TLQ</div>

  <div class="t contact" style="left:508px;top:2184px">nwalcott@TLQ.com &nbsp;<span class="sep">|</span>&nbsp; <b>555-014-2286</b> &nbsp;<span class="sep">|</span>&nbsp; NWALCOTT.COM</div>
  <div class="t contact" style="left:508px;top:2236px">WWW.<b>NWALCOTTFAIRWAY</b>.COM</div>
</div>
</body>
</html>
```